Business Card & Stationary Design Project

We are looking for some creative direction for business cards and our stationary.

We are a global logistics firm that has recently changed its name to Marrick Global Logistics and we have a new website due out tomorrow (www.marrick.com.au).

The colours of the company are rich navy tones, I would like to have business cards that fit together to make one picture on the back (possibly an old map of the world??), and the front to be modern contemporary looking.

But I am open to suggestions, so just incorporate our new logo and get going!
Updates

Hi Everyone,

Thank you for all of your designs so far and the time you have put into it.

I have asked many of you for amendments to see if we can get a final product, so with this in mind I am extending the deadline by a few days.

Good luck and thank you once again.

Please message me direct if you need any clarification.

Kind Regards
Colin

Reason: As outlined the extra 3 days is for amendments and changes to the current submissions. Thanks Colin

Industry/Entity Type

Business

```html
<!DOCTYPE html>
<html lang="en">
<head>
<meta charset="utf-8">
<title>Marrick Global Logistics – Business Card</title>
<link rel="stylesheet" href="https://fonts.googleapis.com/css2?family=Exo+2:wght@400;500&display=swap">
<style>
  :root {
    --navy: #0b2169;
    --navy-deep: #03206f;
    --cyan: #52dcf2;
    --white: #ffffff;
    --stripe: #6e7fa8;
    --globe: #1f63d6;
  }
  html, body {
    margin: 0;
    padding: 0;
    width: 990px;
    height: 1200px;
    overflow: hidden;
    background: var(--white);
    font-family: "Exo 2", sans-serif;
  }
  .sheet {
    position: relative;
    width: 990px;
    height: 1200px;
    background: var(--white);
  }
  .band { position: absolute; left: 0; width: 990px; }

  /* front of card */
  .front-top { top: 0; height: 289px; background: var(--white); }
  .accent-line { top: 290px; height: 5px; background: var(--cyan); }
  .hatch {
    top: 295px; height: 8px;
    background: repeating-linear-gradient(-60deg, var(--stripe) 0 5px, var(--navy) 5px 10px);
  }
  .front-bottom { top: 303px; height: 291px; background: var(--navy); }

  /* back panels */
  .back-panel-a { top: 606px; height: 192px; background: var(--navy-deep); }
  .back-logo-strip { top: 798px; height: 211px; background: var(--white); }
  .back-panel-b { top: 1009px; height: 191px; background: var(--navy-deep); }

  /* wordmark */
  .wordmark {
    position: absolute;
    color: var(--navy);
    font-weight: 500;
    line-height: 1;
    text-transform: uppercase;
  }
  .wordmark .name { display: block; }
  .wordmark .tagline { display: block; }
  .wordmark--small { left: 33px; top: 114px; }
  .wordmark--small .name { font-size: 30px; letter-spacing: 10px; }
  .wordmark--small .tagline { font-size: 10.5px; letter-spacing: 5.4px; margin-top: 4px; }
  .wordmark--large { left: 236px; top: 861px; }
  .wordmark--large .name { font-size: 40px; letter-spacing: 14px; }
  .wordmark--large .tagline { font-size: 14px; letter-spacing: 7.6px; margin-top: 6px; }

  .mark-circle { position: absolute; border-radius: 50%; background: radial-gradient(circle at 35% 30%, #7fb6ff, var(--globe) 55%, #0b3a9c); }
  .mark-circle--small { left: 279px; top: 77px; width: 106px; height: 106px; }
  .mark-circle--large { left: 582px; top: 811px; width: 148px; height: 148px; }

  /* identity on navy */
  .company {
    position: absolute; left: 72px; top: 385px; margin: 0;
    color: var(--cyan); font-weight: 500; font-size: 49px; line-height: 1;
  }
  .company-sub {
    position: absolute; left: 69px; top: 445px; margin: 0;
    color: var(--white); font-weight: 400; font-size: 25px; line-height: 1;
  }

  .contact {
    position: absolute; left: 558px; top: 338px;
    margin: 0; padding: 0; list-style: none;
    color: var(--white); font-size: 22px; line-height: 1;
  }
  .contact li {
    display: flex; align-items: center;
    height: 30px; margin-bottom: 10.5px;
  }
  .contact svg { width: 26px; height: 26px; margin-right: 14px; flex: none; }
  .address {
    position: absolute; left: 598px; top: 507px; margin: 0;
    color: var(--white); font-size: 22px; line-height: 33px; font-style: normal;
  }
</style>
</head>
<body>
<main class="sheet">
  <!-- front -->
  <section class="band front-top"></section>
  <div class="wordmark wordmark--small">
    <span class="name">Marrick</span>
    <span class="tagline">Global Logistics</span>
  </div>
  <div class="mark-circle mark-circle--small"></div>

  <div class="band accent-line"></div>
  <div class="band hatch"></div>
  <section class="band front-bottom"></section>

  <h1 class="company">Marrick</h1>
  <p class="company-sub">Global Logistics</p>

  <ul class="contact">
    <li>
      <svg viewBox="0 0 24 24" aria-hidden="true"><path fill="var(--cyan)" d="M6.6 2.5l3 3.4-1.8 2.3c1 2.3 2.8 4.4 5.4 6l2.3-1.8 3.5 3-1.6 3.4C10.5 18.6 4.6 12.6 3.3 4.1z"/><path fill="none" stroke="var(--cyan)" stroke-width="1.6" d="M14 3.5a7 7 0 0 1 6.5 6.5M14 7a3.5 3.5 0 0 1 3 3"/></svg>
      02 8150 4400 / 0400112358
    </li>
    <li>
      <svg viewBox="0 0 24 24" aria-hidden="true"><rect x="6" y="2" width="12" height="6" fill="var(--cyan)"/><rect x="2" y="9" width="20" height="9" rx="2" fill="var(--cyan)"/><rect x="6" y="15" width="12" height="7" fill="var(--white)" stroke="var(--cyan)" stroke-width="1.5"/></svg>
      029150 4417
    </li>
    <li>
      <svg viewBox="0 0 24 24" aria-hidden="true"><rect x="2" y="5" width="20" height="15" fill="var(--cyan)"/><path fill="none" stroke="var(--navy)" stroke-width="2" d="M2 6l10 7 10-7"/></svg>
      colin@marrick.com.au
    </li>
    <li>
      <svg viewBox="0 0 24 24" aria-hidden="true"><g fill="none" stroke="var(--cyan)" stroke-width="2.6" stroke-linecap="round"><path d="M10 14l-3 3a3 3 0 0 1-4-4l4-4a3 3 0 0 1 4 0"/><path d="M14 10l3-3a3 3 0 0 1 4 4l-4 4a3 3 0 0 1-4 0"/></g></svg>
      marrick.com.au
    </li>
  </ul>
  <address class="address">58 Harbour Lane<br>Pyrmont NSW 2009</address>

  <!-- back -->
  <section class="band back-panel-a"></section>
  <section class="band back-logo-strip"></section>
  <div class="wordmark wordmark--large">
    <span class="name">Marrick</span>
    <span class="tagline">Global Logistics</span>
  </div>
  <div class="mark-circle mark-circle--large"></div>
  <section class="band back-panel-b"></section>
</main>
</body>
</html>
```